Rory's Personal Training -> also needs a logo

Services Frankston, Mornington, and Somerville

Specializes in in-home personal training

BlastCore style workouts

Not really preferential colors but needs to look modern and not stock photo

Training

• 30% off first time customers on a package of 10

```html
<!DOCTYPE html>
<html lang="en">
<head>
<meta charset="utf-8">
<title>Rory's Personal Training</title>
<link rel="stylesheet" href="https://fonts.googleapis.com/css2?family=Barlow+Condensed:wght@600;700&family=Barlow:wght@300;400;600;700&display=swap">
<style>
  :root {
    --sky-top: #6fd0c6;
    --sky-mid: #a9dccf;
    --horizon: #f1eadb;
    --road-far: #8a8178;
    --road-near: #2f2a26;
    --panel: rgba(20, 20, 20, 0.62);
    --band: #205a7d;
    --white: #ffffff;
    --ink: #3a3b3a;
  }
  html, body {
    margin: 0;
    padding: 0;
    overflow: hidden;
    background: #e9e9e9;
  }
  .flyer {
    position: relative;
    width: 1200px;
    height: 900px;
    overflow: hidden;
    font-family: "Barlow", Arial, sans-serif;
    color: var(--white);
  }
  .hero-photo {
    position: absolute;
    left: 0;
    top: 0;
    width: 1200px;
    height: 708px;
    background:
      linear-gradient(180deg,
        var(--sky-top) 0%,
        var(--sky-mid) 35%,
        var(--horizon) 58%,
        var(--road-far) 64%,
        #5a524b 78%,
        var(--road-near) 100%);
  }
  .headline {
    position: absolute;
    left: 678px;
    top: 92px;
    margin: 0;
    font-family: "Barlow Condensed", "Arial Narrow", sans-serif;
    font-weight: 700;
    text-transform: uppercase;
    line-height: 1;
  }
  .headline-lead {
    display: block;
    font-size: 84px;
    color: var(--white);
    text-shadow: 0 2px 6px rgba(0,0,0,0.25);
  }
  .headline-rest {
    display: block;
    margin-top: 14px;
    font-size: 64px;
    line-height: 67px;
    color: var(--ink);
  }
  .info-panel {
    position: absolute;
    left: 0;
    width: 600px;
    background: var(--panel);
    box-sizing: border-box;
    padding-left: 48px;
    text-transform: uppercase;
  }
  .info-panel--specialty {
    top: 407px;
    height: 125px;
    padding-top: 22px;
    font-size: 31px;
    line-height: 42px;
  }
  .info-panel--style {
    top: 567px;
    height: 141px;
    padding-top: 28px;
    font-size: 37px;
    line-height: 50px;
  }
  .info-panel p { margin: 0; }
  .info-light { font-weight: 400; }
  .info-strong { font-weight: 600; }
  .info-thin { font-weight: 300; }
  .service-band {
    position: absolute;
    left: 0;
    top: 708px;
    width: 1200px;
    height: 192px;
    background: var(--band);
  }
  .service-areas {
    position: absolute;
    left: 48px;
    top: 26px;
    margin: 0;
    font-size: 21px;
    font-weight: 600;
    letter-spacing: 0.4px;
    text-transform: uppercase;
  }
  .brand-name {
    position: absolute;
    left: 790px;
    top: 30px;
    margin: 0;
    font-family: "Barlow Condensed", "Arial Narrow", sans-serif;
    font-weight: 700;
    color: var(--white);
    text-transform: uppercase;
    line-height: 1;
  }
  .brand-name-main {
    display: block;
    font-size: 84px;
    letter-spacing: 2px;
  }
  .brand-name-sub {
    display: block;
    margin-top: 4px;
    font-size: 34px;
    letter-spacing: 1px;
  }
</style>
</head>
<body>
  <main class="flyer">
    <div class="hero-photo" role="img" aria-label="Photograph of an open asphalt road with a white centre line stretching to the horizon under a teal sky with soft pink clouds"></div>

    <h1 class="headline">
      <span class="headline-lead">Get Fit</span>
      <span class="headline-rest">And Change<br>The Way You Live</span>
    </h1>

    <section class="info-panel info-panel--specialty">
      <p class="info-light">Specializes in</p>
      <p class="info-strong">In-home personal training</p>
    </section>

    <section class="info-panel info-panel--style">
      <p class="info-light">BlastCore style</p>
      <p class="info-thin">Workouts</p>
    </section>

    <footer class="service-band">
      <p class="service-areas">Services Frankston, Mornington, and Somerville</p>
      <p class="brand-name">
        <span class="brand-name-main">Rory's</span>
        <span class="brand-name-sub">Personal Training</span>
      </p>
    </footer>
  </main>
</body>
</html>
```